Business card for Chiropractic clinics needs reworked / redesigned

The business card in attachment was designed 10 years ago. It is in need of an update.
We have 2 clinics:
VELDHOVE KLINIEK & VELDHOVE KLINIEK NOORD
Only one address needs to be on the card for doctors that only work in one clinic and two addresses need to be on the card for the doctors that work in both clinics.

Target Market(s)

patients/referrers

Industry/Entity Type

Medical

Contact Information for Business Card

Logo (in full or zoomed-in)
Clinic Name
Doctor name and title
clinic address, website, tel, email

Font styles to use
Sans Serif

Colors

Designer to choose colors to be used in the design.

Requirements
Must have
• Good contrast/readability
• We like modern minimalistic designs
• The Bcard needs to project our very high standard of proficiency/professionalism
Should not have
• Not curly
• Not to much colours

```html
<!DOCTYPE html>
<html lang="nl">
<head>
<meta charset="utf-8">
<title>Veldhove Kliniek – visitekaartje</title>
<link href="https://fonts.googleapis.com/css2?family=Source+Sans+3:wght@400;600;700&display=swap" rel="stylesheet">
<style>
  :root{
    --sage:#4f6e61;
    --sage-light:#6f9e86;
    --ink:#2f4a40;
    --text:#3a3f3c;
    --cream:#f4f4e8;
    --page:#e9e7e1;
    --on-sage:#eef0ea;
  }
  html,body{margin:0;padding:0;overflow:hidden}
  body{
    width:1200px;height:800px;background:var(--page);
    display:flex;align-items:center;justify-content:center;gap:60px;
    font-family:"Source Sans 3",sans-serif;
  }
  .card{
    width:525px;height:300px;border-radius:18px;position:relative;
    box-shadow:0 10px 30px rgba(0,0,0,.12);overflow:hidden;
  }
  .card--front{background:var(--sage);display:flex;align-items:center;justify-content:center}
  .brand{display:flex;align-items:center;gap:16px;color:var(--on-sage)}
  .brand__dot{width:18px;height:18px;border-radius:50%;background:var(--on-sage)}
  .brand__names{font-size:24px;letter-spacing:1.5px;line-height:1.15;font-weight:400}
  .card--back{background:var(--cream);color:var(--text)}
  .person{position:absolute;left:0;right:0;top:118px;text-align:center}
  .person__name{font-weight:700;font-size:24px;letter-spacing:5px;color:var(--ink)}
  .person__title{font-weight:600;font-size:14px;letter-spacing:1.5px;color:var(--sage-light);margin-top:2px}
  .clinic{position:absolute;font-size:15px;line-height:1.45}
  .clinic__label{font-size:11px;color:var(--sage-light);text-transform:uppercase;letter-spacing:.3px}
  .clinic__row{display:flex;align-items:center;gap:7px}
  .clinic--main{top:22px;right:24px;text-align:right}
  .clinic--main .clinic__row{justify-content:flex-end}
  .clinic--north{bottom:20px;left:24px}
  .icon{width:12px;height:12px;fill:var(--ink);flex:none}
</style>
</head>
<body>
  <svg width="0" height="0" style="position:absolute">
    <symbol id="i-pin" viewBox="0 0 12 12"><path d="M6 0a4.2 4.2 0 0 0-4.2 4.2C1.8 7.4 6 12 6 12s4.2-4.6 4.2-7.8A4.2 4.2 0 0 0 6 0zm0 5.8a1.6 1.6 0 1 1 0-3.2 1.6 1.6 0 0 1 0 3.2z"/></symbol>
    <symbol id="i-phone" viewBox="0 0 12 12"><path d="M1 3.5C1 2 3 1.5 6 1.5s5 .5 5 2v1.3H8.5V3.8h-5v1H1zM2.5 5.5h7l1.5 5H1zM6 6.7a1.4 1.4 0 1 0 0 2.8 1.4 1.4 0 0 0 0-2.8z"/></symbol>
    <symbol id="i-mail" viewBox="0 0 12 12"><path d="M0 2.5h12v7H0zM1 3.3l5 3.6 5-3.6v-.1H1z"/></symbol>
    <symbol id="i-web" viewBox="0 0 12 12"><circle cx="6" cy="6" r="5.5"/><path d="M.8 6h10.4M6 .5v11M2 3h8M2 9h8" stroke="var(--cream)" stroke-width=".8" fill="none"/></symbol>
  </svg>

  <section class="card card--front">
    <div class="brand">
      <span class="brand__dot"></span>
      <div class="brand__names">
        <div>VELDHOVE KLINIEK</div>
        <div>VELDHOVE KLINIEK NOORD</div>
      </div>
    </div>
  </section>

  <section class="card card--back">
    <div class="clinic clinic--main">
      <div class="clinic__row clinic__label">Veldhove Kliniek <svg class="icon"><use href="#i-pin"/></svg></div>
      <div class="clinic__row">Lindenlaan 148</div>
      <div class="clinic__row">09 555 01 42 <svg class="icon"><use href="#i-phone"/></svg></div>
      <div class="clinic__row">info@veldhove.be <svg class="icon"><use href="#i-mail"/></svg></div>
      <div class="clinic__row">veldhovekliniek.be <svg class="icon"><use href="#i-web"/></svg></div>
    </div>

    <div class="person">
      <div class="person__name">MAARTEN VERHULST</div>
      <div class="person__title">CHIROPRACTOR</div>
    </div>

    <div class="clinic clinic--north">
      <div class="clinic__row clinic__label"><svg class="icon"><use href="#i-pin"/></svg> Veldhove Kliniek Noord</div>
      <div class="clinic__row">Molenstraat 41</div>
      <div class="clinic__row"><svg class="icon"><use href="#i-phone"/></svg> 09 555 02 87</div>
      <div class="clinic__row"><svg class="icon"><use href="#i-mail"/></svg> info@veldhove.be</div>
      <div class="clinic__row"><svg class="icon"><use href="#i-web"/></svg> veldhovenoord.be</div>
    </div>
  </section>
</body>
</html>
```